kestrel home systems HERS

Looking for business card design that represents our company. we are kestrel home systems and we dedicate our skills of home energy efficiency to our customer by providing energy solution to their energy problems.
HVAC
SOLAR
INSULLATION
LIGHTING
DUCT TESTING
HERS RATING.

```html
<!DOCTYPE html>
<html lang="en">
<head>
<meta charset="utf-8">
<title>Kestrel Home Systems – Business Card</title>
<link href="https://fonts.googleapis.com/css2?family=Montserrat:wght@400;700;800&family=Open+Sans:wght@400&display=swap" rel="stylesheet">
<style>
  :root {
    --bg: #2a2a2a;
    --card: #0d0d0d;
    --card-edge: #1a1a1a;
    --green: #8fd13b;
    --blue: #2aa6e0;
    --white: #f2f2f2;
  }
  * { box-sizing: border-box; margin: 0; padding: 0; }
  html, body { width: 1200px; height: 1200px; overflow: hidden; }
  body {
    background: var(--bg);
    display: flex;
    flex-direction: column;
    align-items: center;
    justify-content: center;
    gap: 44px;
    font-family: "Montserrat", sans-serif;
  }
  .card {
    position: relative;
    width: 900px;
    height: 514px;
    background: radial-gradient(ellipse at 60% 30%, #181818 0%, var(--card) 70%);
    border: 1px solid var(--card-edge);
    border-radius: 22px;
    box-shadow: 0 18px 40px rgba(0,0,0,0.55);
  }
  .brand {
    display: flex;
    align-items: center;
    gap: 16px;
  }
  .brand-dot {
    width: 44px;
    height: 44px;
    border-radius: 50%;
    background: var(--blue);
    flex: none;
  }
  .brand-name {
    color: var(--green);
    font-weight: 800;
    font-size: 40px;
    line-height: 1.05;
    letter-spacing: 1px;
    text-transform: uppercase;
  }
  .card-front .brand {
    position: absolute;
    left: 50%;
    top: 170px;
    transform: translateX(-50%);
  }
  .services {
    position: absolute;
    left: 0;
    right: 0;
    bottom: 62px;
    display: flex;
    justify-content: center;
    align-items: center;
    gap: 14px;
    color: var(--green);
    font-weight: 700;
    font-size: 19px;
    letter-spacing: 0.6px;
    text-transform: uppercase;
  }
  .services .sep {
    width: 9px;
    height: 9px;
    border-radius: 50%;
    background: var(--blue);
  }
  .person {
    position: absolute;
    left: 60px;
    top: 58px;
  }
  .person-name {
    color: var(--green);
    font-weight: 800;
    font-size: 34px;
    letter-spacing: 2px;
    text-transform: uppercase;
  }
  .person-role {
    color: var(--blue);
    font-weight: 400;
    font-size: 26px;
    margin-top: 2px;
  }
  .card-back .brand {
    position: absolute;
    right: 70px;
    top: 150px;
  }
  .card-back .brand-name { font-size: 34px; }
  .contact {
    position: absolute;
    left: 60px;
    bottom: 62px;
    list-style: none;
    font-family: "Open Sans", sans-serif;
    color: var(--white);
    font-size: 22px;
  }
  .contact li {
    display: flex;
    align-items: center;
    gap: 16px;
    margin-top: 6px;
  }
  .contact svg { width: 24px; height: 24px; flex: none; }
  .address {
    position: absolute;
    right: 70px;
    bottom: 62px;
    text-align: right;
    font-family: "Open Sans", sans-serif;
    color: var(--white);
    font-size: 23px;
    line-height: 1.45;
    font-style: normal;
  }
</style>
</head>
<body>

  <section class="card card-front">
    <div class="brand">
      <span class="brand-dot"></span>
      <span class="brand-name">Kestrel<br>Home Systems</span>
    </div>
    <div class="services">
      <span>HVAC</span><span class="sep"></span>
      <span>Solar</span><span class="sep"></span>
      <span>Insullation</span><span class="sep"></span>
      <span>Lighting</span><span class="sep"></span>
      <span>Duct Testing</span><span class="sep"></span>
      <span>HERS Rating.</span>
    </div>
  </section>

  <section class="card card-back">
    <div class="person">
      <div class="person-name">Marcus Hale</div>
      <div class="person-role">CEO</div>
    </div>

    <div class="brand">
      <span class="brand-dot"></span>
      <span class="brand-name">Kestrel<br>Home Systems</span>
    </div>

    <ul class="contact">
      <li>
        <svg viewBox="0 0 24 24" aria-hidden="true"><path fill="#2aa6e0" d="M6.6 10.8c1.4 2.8 3.8 5.1 6.6 6.6l2.2-2.2c.3-.3.7-.4 1-.2 1.1.4 2.3.6 3.6.6.6 0 1 .4 1 1V20c0 .6-.4 1-1 1C10.6 21 3 13.4 3 4c0-.6.4-1 1-1h3.5c.6 0 1 .4 1 1 0 1.3.2 2.5.6 3.6.1.3 0 .7-.2 1l-2.3 2.2z"/></svg>
        <span>028-555-0192</span>
      </li>
      <li>
        <svg viewBox="0 0 24 24" aria-hidden="true"><rect x="2" y="5" width="20" height="14" rx="1.5" fill="#2aa6e0"/><path d="M3 6l9 7 9-7" fill="none" stroke="#0d0d0d" stroke-width="1.6"/></svg>
        <span>marcushale@kestrelhomesystems.com</span>
      </li>
      <li>
        <svg viewBox="0 0 24 24" aria-hidden="true"><g fill="none" stroke="#2aa6e0" stroke-width="1.6"><circle cx="12" cy="12" r="9.5"/><ellipse cx="12" cy="12" rx="4.2" ry="9.5"/><path d="M2.5 12h19M4 7h16M4 17h16"/></g></svg>
        <span>www.kestrelhomesystems.com</span>
      </li>
    </ul>

    <address class="address">
      #214 1190 Alder Row<br>
      Northbay Canada
    </address>
  </section>

</body>
</html>
```